Building company buisness cards

We are looking for a sharp modern new look for our business cards.We are a New Zealand based company that specialises in house and land packages.We have attached a photo of the current logo and would like to see if it can be improved somehow if needed.We are open to any colours but we have chosen Black and White at this stage. Feel free to change the font and make the logo smarter looking.Play with the colours and see what looks best.We want a card that looks so good know one will want to throw it away!

Target Market(s)

Building profesonals, home buyers

Industry/Entity Type

Building

Contact Information for Business Card

Derek Haskins
0274930268
derekh@stonerange.co.nz

Font styles to use
Serif
Sans Serif

Colors

Designer to choose colors to be used in the design.

Requirements
Must have
• Just the logo on one side and details on the other
• Clean simple looking card
Nice to have
• Round corners and detail like raised or spot UV
• Something that stands out
Should not have
• To title needed, Director etc

```html
<!DOCTYPE html>
<html lang="en">
<head>
<meta charset="utf-8">
<title>Stonerange Business Cards</title>
<link rel="stylesheet" href="https://fonts.googleapis.com/css2?family=Lato:wght@400;700;900&display=swap">
<style>
  :root {
    --backdrop: #8a8a8a;
    --card-dark: #0d0d0d;
    --card-light: #ffffff;
    --ink: #111111;
    --ink-soft: #4a4a4a;
    --paper-text: #ffffff;
  }
  * { margin: 0; padding: 0; box-sizing: border-box; }
  html, body {
    width: 1200px; height: 1200px; overflow: hidden;
    background: var(--backdrop);
    font-family: "Lato", sans-serif;
  }
  .canvas { position: relative; width: 1200px; height: 1200px; }

  .card {
    position: absolute;
    width: 760px; height: 434px;
    border-radius: 38px;
    overflow: hidden;
    box-shadow: 0 18px 40px rgba(0,0,0,0.35);
  }
  .card--back { left: 360px; top: 120px; background: var(--card-dark); }
  .card--front { left: 80px; top: 640px; background: var(--card-light); }

  .brand { position: absolute; }
  .brand__name {
    display: block;
    font-weight: 900;
    font-size: 58px;
    line-height: 1;
    letter-spacing: -1px;
  }
  .brand__tagline {
    font-weight: 400;
    font-size: 16px;
    letter-spacing: 0.5px;
    margin-top: 8px;
  }

  .card--back .brand { left: 50%; top: 50%; transform: translate(-50%, -50%); color: var(--paper-text); }
  .card--front .brand { right: 60px; top: 190px; color: var(--ink); }
  .card--front .brand__name { font-size: 52px; }
  .card--front .brand__tagline { color: var(--ink-soft); }

  .edge-tab {
    position: absolute;
    left: 0; top: 60px;
    width: 20px; height: 44px;
    background: var(--ink);
  }
  .details { position: absolute; left: 60px; top: 56px; color: var(--ink); }
  .details__name { font-weight: 700; font-size: 30px; line-height: 1.1; }
  .details__role { font-size: 17px; color: var(--ink-soft); margin-top: 4px; }
  .contact { list-style: none; margin-top: 22px; }
  .contact__item {
    display: flex; align-items: center; gap: 12px;
    font-size: 19px; line-height: 1.7; color: var(--ink);
  }
  .contact__icon { width: 18px; height: 18px; flex: none; }
</style>
</head>
<body>
<main class="canvas">

  <section class="card card--back" aria-label="Card back">
    <div class="brand">
      <span class="brand__name">Stonerange</span>
      <p class="brand__tagline">Houses shaped for life.</p>
    </div>
  </section>

  <section class="card card--front" aria-label="Card front">
    <div class="edge-tab"></div>

    <div class="details">
      <h1 class="details__name">Derek Haskins</h1>
      <p class="details__role">Managing Director</p>
      <ul class="contact">
        <li class="contact__item">
          <svg class="contact__icon" viewBox="0 0 24 24" aria-hidden="true">
            <circle cx="12" cy="12" r="11" fill="none" stroke="#555" stroke-width="2"/>
            <path d="M8 7c1 0 1.5 2 1.5 2.5S8.5 11 8.5 11a7 7 0 0 0 4.5 4.5s.8-1 1.5-1 2.5.5 2.5 1.5-1 2-2 2C10 18 6 14 6 9c0-1 1-2 2-2z" fill="#555"/>
          </svg>
          <span>0274930268</span>
        </li>
        <li class="contact__item">
          <svg class="contact__icon" viewBox="0 0 24 24" aria-hidden="true">
            <rect x="2" y="5" width="20" height="14" fill="#555"/>
            <path d="M2 5l10 8 10-8" fill="none" stroke="#fff" stroke-width="1.6"/>
          </svg>
          <span>derekh@stonerange.co.nz</span>
        </li>
        <li class="contact__item">
          <svg class="contact__icon" viewBox="0 0 24 24" aria-hidden="true">
            <circle cx="12" cy="12" r="11" fill="#777"/>
            <path d="M1 12h22M12 1v22M4 6h16M4 18h16" stroke="#fff" stroke-width="1.2" fill="none"/>
            <ellipse cx="12" cy="12" rx="5" ry="11" fill="none" stroke="#fff" stroke-width="1.2"/>
          </svg>
          <span>www.stonerange.co.nz</span>
        </li>
      </ul>
    </div>

    <div class="brand">
      <span class="brand__name">Stonerange</span>
      <p class="brand__tagline">Houses shaped for life.</p>
    </div>
  </section>

</main>
</body>
</html>
```